Mandarin tuition, language and travel services

We need a website for a new startup company, which offers Mandarin tuition, translating and interpreting, and travel services. Our company is based in Jersey, a British channel island. We would like a creative and modern professional website. Preferably with some animations. The attached is a website, which style we would prefer:
http://www.quorvabelt.net/
We have also attached our logo for your reference
We would also like to see designs using black, red and orange, which corresponds with our logo colours. The cartoon images could be travel resorts in China, and the president of China waving to the web-browsers. Of course, we wouldn't wish to restrain the designers creativity. Any creative and interesting ideas are welcomed! We look forward to hearing from you!

Target Market(s)

school children and adults

Industry/Entity Type

It Company

Number of Pages Required

3 page

Requirements
Must have
• We would prefer a small 3 pages website, if possible. The 3 pages need to be Services, News Room, and Contact us.

```html
<!DOCTYPE html>
<html lang="en">
<head>
<meta charset="utf-8">
<title>Lantern Mandarin</title>
<link rel="stylesheet" href="https://fonts.googleapis.com/css2?family=Noto+Serif&family=Lato:wght@300;400&display=swap">
<style>
:root{
  --red:#d8202a;
  --red-dark:#a5121a;
  --orange:#dd6c06;
  --orange-shadow:#c9a37d;
  --black:#000;
  --grey-shadow:#bdbdbd;
  --white:#fff;
  --text:#1a1a1a;
  --serif:'Noto Serif', Georgia, serif;
  --sans:'Lato', Arial, sans-serif;
}
*{margin:0;padding:0;box-sizing:border-box}
html,body{width:1200px;height:1108px;overflow:hidden;background:var(--white)}
body{position:relative;font-family:var(--sans);color:var(--text)}
.hero{position:absolute;left:0;top:0;width:1200px;height:516px;
  background:radial-gradient(ellipse at 70% 40%,#b3581e 0%,#8a3d14 35%,#4a2210 70%,#2a1a12 100%)}
.brand{position:absolute;left:132px;top:0;width:158px;height:122px}
.brand svg{position:absolute;inset:0}
.brand-name{position:absolute;left:0;right:0;top:30px;text-align:center;font-family:var(--serif);font-size:19px;line-height:24px;color:var(--black)}
.nav{position:absolute;top:42px;left:0;font-family:var(--serif);font-size:14.5px}
.nav a{position:absolute;white-space:nowrap;color:var(--white);text-decoration:none}
.hero-title{position:absolute;left:188px;top:218px;font-family:var(--serif);font-weight:400;font-size:40px;color:var(--red)}
.hero-lead{position:absolute;left:188px;top:280px;width:460px;font-weight:300;font-size:23px;line-height:29px;color:var(--white)}
.hero-btn{position:absolute;left:188px;top:362px;width:137px;height:42px;background:var(--black);color:var(--red);font-size:15px;line-height:42px;text-align:center;font-weight:300}
.dots{position:absolute;left:193px;top:436px;display:flex;gap:10px}
.dots span{width:8px;height:8px;border-radius:50%;background:var(--red)}
.dots span.active{background:#f07a10}
.service{position:absolute;top:465px;width:302px;height:210px;color:var(--white)}
.service::before{content:"";position:absolute;left:-6px;top:8px;width:302px;height:210px;background:var(--grey-shadow);z-index:-1}
.service.tuition{left:132px;background:var(--orange)}
.service.tuition::before{background:var(--orange-shadow)}
.service.translating{left:449px;background:var(--black)}
.service.travel{left:766px;background:var(--black)}
.service h2{position:absolute;left:32px;top:17px;font-family:var(--serif);font-weight:400;font-size:39px;line-height:45px}
.service .more{position:absolute;left:38px;top:134px;font-size:15px;font-weight:300;display:flex;align-items:center;gap:10px}
.service .icon{position:absolute;left:218px;top:124px;width:66px;height:66px;border-radius:50%;display:flex;align-items:center;justify-content:center;background:var(--red)}
.service.tuition .icon{background:var(--black)}
.about{position:absolute;left:161px;top:696px;width:568px}
.section-title{font-family:var(--serif);font-weight:400;font-size:38px;line-height:46px;color:var(--black)}
.about p{margin-top:12px;font-size:12px;line-height:24px;text-align:justify}
.btn-red{display:inline-block;width:105px;height:35px;background:var(--red);border-bottom:3px solid var(--red-dark);color:var(--white);font-size:12px;line-height:33px;text-align:center;border-radius:2px}
.about .btn-red{margin-top:12px}
.divider{position:absolute;left:757px;top:708px;width:1px;height:230px;background:#e3e3e3}
.news{position:absolute;left:778px;top:703px;width:278px}
.date{display:inline-block;margin-top:10px;background:var(--red);color:var(--white);font-family:var(--serif);font-size:9.5px;height:16px;line-height:16px;padding:0 9px}
.news p{margin-top:6px;font-size:12px;line-height:19.2px;text-align:justify}
.news .btn-red{margin-top:13px}
.footer{position:absolute;left:0;top:973px;width:1200px;height:135px;background:var(--black);color:var(--white)}
.footer-nav a{position:absolute;top:40px;font-family:var(--serif);font-size:14.5px;color:var(--white);text-decoration:none}
.social{position:absolute;left:176px;top:77px;display:flex;gap:6px}
.social span{width:26px;height:26px;border-radius:4px;background:#5c5c5c}
.footer-brand{position:absolute;left:944px;top:38px;font-family:var(--serif);font-size:15px;line-height:19px;text-align:center;width:100px;color:var(--white)}
.copyright{position:absolute;left:864px;top:100px;font-size:11px;font-weight:300}
</style>
</head>
<body>
<header class="hero" role="img" aria-label="Photograph of the Great Wall winding over autumn hills in warm orange light">
  <div class="brand">
    <svg width="158" height="122" viewBox="0 0 158 122"><polygon points="0,0 158,0 158,84 79,122 0,84" fill="#fff"/></svg>
    <div class="brand-name">Lantern<br>Mandarin</div>
  </div>
  <nav class="nav">
    <a style="left:582px">Home</a>
    <a style="left:656px">About Us</a>
    <a style="left:748px">Services</a>
    <a style="left:838px">News room</a>
    <a style="left:950px">Contact us</a>
  </nav>
  <h1 class="hero-title">Lantern Mandarin</h1>
  <p class="hero-lead">We offer Mandarin tuition, translating and interpreting, and travel services.</p>
  <div class="hero-btn">LEARN MORE</div>
  <div class="dots"><span></span><span></span><span class="active"></span><span></span></div>
</header>

<section class="service tuition">
  <h2>Mandarine<br>Tution</h2>
  <div class="more">LEARN MORE <svg width="9" height="12" viewBox="0 0 9 12"><polygon points="0,0 9,6 0,12" fill="#fff"/></svg></div>
  <div class="icon"><svg width="40" height="30" viewBox="0 0 40 30"><polygon points="20,2 39,10 20,18 1,10" fill="#fff"/><path d="M9 14v7c0 4 22 4 22 0v-7l-11 5z" fill="#fff"/><rect x="34" y="10" width="2" height="12" fill="#fff"/></svg></div>
</section>
<section class="service translating">
  <h2>Translating &amp;<br>Interpreting</h2>
  <div class="more">LEARN MORE <svg width="9" height="12" viewBox="0 0 9 12"><polygon points="0,0 9,6 0,12" fill="#fff"/></svg></div>
  <div class="icon"><svg width="32" height="30" viewBox="0 0 32 30"><path d="M4 20v-4a12 12 0 0 1 24 0v4" fill="none" stroke="#fff" stroke-width="4"/><rect x="2" y="17" width="8" height="12" rx="2" fill="#fff"/><rect x="22" y="17" width="8" height="12" rx="2" fill="#fff"/></svg></div>
</section>
<section class="service travel">
  <h2>Travel<br>Services</h2>
  <div class="more">LEARN MORE <svg width="9" height="12" viewBox="0 0 9 12"><polygon points="0,0 9,6 0,12" fill="#fff"/></svg></div>
  <div class="icon"><svg width="30" height="30" viewBox="0 0 30 30"><g transform="rotate(45 15 15)"><path d="M15 1c2 0 2 3 2 5v6l11 6v3l-11-3v6l3 2v2l-5-1-5 1v-2l3-2v-6l-11 3v-3l11-6v-6c0-2 0-5 2-5z" fill="#fff"/></g></svg></div>
</section>

<section class="about">
  <h2 class="section-title">About Us</h2>
  <p>Conubia vulputate dolor lectus suscipit vestibulum at ad semper nascetur id mollis class tincidunt curabitur a commodo porta parturient ac parturient adipiscing blandit lectus ac ad condimentum condimentum.Leo suspendisse quam sagittis curæ vestibulum. Parturient a a viverra habitant ad euismod varius commodo hendrerit neque facilisi condimentum ad etiam amet imperdiet ut convallis feugiat a urna arcu sit orci.Platea auctor a sem a eu condimentum per parturient porta ullamcorper libero eu dignissim et eget a imperdiet est aliquam.Integer sed.</p>
  <span class="btn-red">LEARN MORE</span>
</section>
<div class="divider"></div>
<section class="news">
  <h2 class="section-title">News</h2>
  <span class="date">12-jan-2016</span>
  <p>Vestibulum at ad semper nascetur id mollis class tincidunt curabitur a commodo porta parturient ac parturient adipiscing blandit lectus ac ad condimentum condimentum.Leo suspendisse quam sagittis curæ vestibulum.</p>
  <span class="btn-red">READ MORE</span>
</section>

<footer class="footer">
  <nav class="footer-nav">
    <a style="left:172px">Home</a>
    <a style="left:246px">About Us</a>
    <a style="left:338px">Services</a>
    <a style="left:429px">News room</a>
    <a style="left:541px">Contact us</a>
  </nav>
  <div class="social" aria-label="Social links"><span></span><span></span><span></span><span></span></div>
  <div class="footer-brand">Lantern<br>Mandarin</div>
  <div class="copyright">© 2016. www.companyname.com</div>
</footer>
</body>
</html>
```